Business cards - KESTO Roofing & Siding

We need simple business cards made up for our Roofing & Siding business based in Calgary Alberta.
The logo on one side of the card and potentially our slogan "Built with trust, verified by time".
The other side could have:
-A small logo
-Rep name:
-Rep cell phone:
-Rep email:
-Office phone: 403-386-2049
-Website: PrairieShinglePros.com

We would like to incorporate the colours from our logo, especially the lite blue on the jpeg file. I have attached the ai file and jpeg file. We like the colours better on the jpeg file.

I do not require a money back guarantee

```html
<!DOCTYPE html>
<html lang="en">
<head>
<meta charset="UTF-8">
<title>KESTO Roofing &amp; Siding – Business Cards</title>
<link rel="stylesheet" href="https://fonts.googleapis.com/css2?family=Montserrat:wght@400;600&family=Oswald:wght@500&display=swap">
<style>
  :root {
    --stage: #161616;
    --card-dark: #1c1c1c;
    --card-mid: #2c2c2c;
    --brand-blue: #1e8fe6;
    --text-white: #f2f2f2;
  }
  * { margin: 0; padding: 0; box-sizing: border-box; }
  html, body {
    width: 1200px; height: 900px; overflow: hidden;
    background: var(--stage);
  }
  .stage {
    width: 1200px; height: 900px;
    display: flex; flex-direction: column;
    align-items: center; justify-content: center; gap: 40px;
  }
  .card {
    position: relative;
    width: 680px; height: 389px;
    overflow: hidden;
    box-shadow: 0 12px 30px rgba(0,0,0,.55);
  }
  .card-pattern {
    position: absolute; inset: 0;
    background: radial-gradient(ellipse at 55% 40%, var(--card-mid), var(--card-dark) 75%);
  }
  .card-content { position: relative; height: 100%; }

  /* Front */
  .front .card-content {
    display: flex; align-items: center; justify-content: center; gap: 14px;
  }
  .brand-mark {
    width: 22px; height: 22px; background: var(--brand-blue);
  }
  .brand-name {
    font-family: "Montserrat", sans-serif; font-weight: 600;
    font-size: 26px; letter-spacing: 4px; color: var(--text-white);
  }

  /* Back */
  .back .card-content {
    display: flex; align-items: center; justify-content: center; gap: 26px;
    padding-top: 10px;
  }
  .rep { text-align: right; }
  .rep-name {
    font-family: "Oswald", sans-serif; font-weight: 500;
    font-size: 38px; letter-spacing: 1px; color: var(--brand-blue);
    line-height: 1;
  }
  .rep-title {
    font-family: "Montserrat", sans-serif; font-weight: 400;
    font-size: 15px; letter-spacing: .5px; color: var(--text-white);
    margin-top: 4px;
  }
  .divider { width: 2px; height: 86px; background: var(--brand-blue); }
  .contact-list { list-style: none; }
  .contact-list li {
    display: flex; align-items: center; gap: 10px;
    font-family: "Montserrat", sans-serif; font-size: 15px;
    color: var(--text-white); line-height: 23px;
  }
  .contact-icon { width: 12px; height: 12px; flex: none; }
</style>
</head>
<body>
<main class="stage">
  <section class="card front">
    <div class="card-pattern" role="img" aria-label="Tone-on-tone maple leaf pattern across the card"></div>
    <div class="card-content">
      <span class="brand-mark"></span>
      <span class="brand-name">KESTO ROOFING &amp; SIDING</span>
    </div>
  </section>

  <section class="card back">
    <div class="card-pattern" role="img" aria-label="Tone-on-tone maple leaf pattern across the card"></div>
    <div class="card-content">
      <div class="rep">
        <p class="rep-name">DANIEL REYES</p>
        <p class="rep-title">DIRECTOR</p>
      </div>
      <span class="divider"></span>
      <ul class="contact-list">
        <li>
          <svg class="contact-icon" viewBox="0 0 12 12"><path d="M2 1h2.5l1 3-1.5 1a6 6 0 0 0 3 3l1-1.5 3 1V10a1 1 0 0 1-1 1A9 9 0 0 1 1 2a1 1 0 0 1 1-1z" fill="var(--brand-blue)"/></svg>
          403-386-2049
        </li>
        <li>
          <svg class="contact-icon" viewBox="0 0 12 12"><rect x="3" y="0.5" width="6" height="11" rx="1" fill="none" stroke="var(--brand-blue)" stroke-width="1.2"/><circle cx="6" cy="9.5" r=".7" fill="var(--brand-blue)"/></svg>
          905-612-4387
        </li>
        <li>
          <svg class="contact-icon" viewBox="0 0 12 12"><rect x=".6" y="2.5" width="10.8" height="7" fill="none" stroke="var(--brand-blue)" stroke-width="1.2"/><path d="M.6 2.5 6 6.5l5.4-4" fill="none" stroke="var(--brand-blue)" stroke-width="1.2"/></svg>
          kestoroof@prairiemail.net
        </li>
        <li>
          <svg class="contact-icon" viewBox="0 0 12 12"><g fill="none" stroke="var(--brand-blue)" stroke-width="1"><circle cx="6" cy="6" r="5.2"/><ellipse cx="6" cy="6" rx="2.3" ry="5.2"/><path d="M.8 6h10.4"/></g></svg>
          PrairieShinglePros.com
        </li>
      </ul>
    </div>
  </section>
</main>
</body>
</html>
```